Wendleby Choir needs a concert poster!

22nd November is Ss Ottoline's Feast, the Patron Saint of music. 100 years ago on that day, Dorian Maltravers was born, famously dubbed the "greatest English composer since Gadsby". 50 years ago that day, three of the most prominent men in history died: this trifecta included theologian and author of 'Quellmark' R. T. Pembury, philosopher and author of 'Silent Tin Harvest' Perrine Vasholt, and one of America's most beloved presidents, Walter G. Ashcombe.

In memory of these prominent figures of the 20th century, the Choir of Holy Ambrose by the Weir Stile (the Market Kirk of Wendleby) perform some of the world's best vocal music composed or inspired by these men. The playlist includes Maltravers's 'Carol for Ss Ottoline', K. D. Ruhnau's 'Geh, Seele, geh', 'The Lantern' by Perrin Vasholt set to music by Miles Tandridge, and Cuthbert Fennimore's 'Lay down, dear one, in quiet rest', written specially for the memorial service of President Walter G Ashcombe in Harrowgate Federal Minster.

We are looking for a dramatic concert poster / or series of posters that encapsulate all these important aspects on this one day. Tickets will be set up on seatpassly.net - space for their logo will be needed.

22nd November 2013, 8pm
Norbury College Chapel, Oxford
Choir of Holy Ambrose by the Weir Stile
Gil Pettifer-Rowe
Tickets: £5

Target Market(s)

Mostly students and staff from the Universities of Wendleby and Marlowe, but also singers from local Oxfordshire choral societies who have a passion for singing and the repertoire. Local musical professionals and appreciators. Not really suitable for children. Cultured adults that support local artistic projects and go to live classical concerts. Higher-end readership. I would like to charge much more for the ticket prices (in order to reflect the quality of the performance) but Oxford is haemorrhaging quality concerts for very little, and the competition is fierce. This poster needs to stand out from the crowd of other events going on, and perhaps be coupled with an inventive marketing strategy.

Industry/Entity Type

Church

Requirements
Must have
• Holy Ambrose by the Weir Stile logo
Seatpassly.net logo

My name prominently displayed

```html
<!DOCTYPE html>
<html lang="en">
<head>
<meta charset="utf-8">
<title>Ss Ottoline's Feast Concert</title>
<link href="https://fonts.googleapis.com/css2?family=Alfa+Slab+One&family=Playball&family=Roboto+Slab:wght@500;700;800&family=Open+Sans:ital,wght@0,600;0,700;0,800;1,700&display=swap" rel="stylesheet">
<style>
:root{
  --parchment:#eadcbc;
  --parchment-edge:#b99f72;
  --bar:#3a2a1c;
  --red:#c8281d;
  --red-dark:#8d1a12;
  --ribbon:#2e7fa3;
  --ribbon-dark:#1d5b78;
  --navy:#13283a;
  --panel:#1f4541;
  --panel-dark:#163532;
  --cream:#f5e6a8;
  --white:#ffffff;
  --ink:#2a2119;
}
*{margin:0;padding:0;box-sizing:border-box}
html,body{width:853px;height:1200px;overflow:hidden;background:var(--parchment)}
.poster{position:relative;width:853px;height:1200px;overflow:hidden;
  background:radial-gradient(ellipse at 55% 40%,#f1e6cb 0%,var(--parchment) 45%,var(--parchment-edge) 100%);
  font-family:'Open Sans',sans-serif;color:var(--ink)}
.date-bar{position:absolute;left:0;top:0;width:853px;height:70px;background:linear-gradient(#2c2015,var(--bar));
  display:flex;align-items:center;justify-content:center}
.date-bar span{font-family:'Alfa Slab One',serif;font-size:34px;color:var(--red);letter-spacing:1px;text-transform:uppercase}
.title{position:absolute;left:0;top:78px;width:853px;text-align:center;font-family:'Alfa Slab One',serif;
  font-size:64px;line-height:1;color:var(--red);text-transform:uppercase;text-shadow:3px 3px 0 var(--red-dark)}
.subtitle{position:absolute;left:0;top:140px;width:853px;text-align:center;font-family:'Playball',cursive;
  font-size:112px;line-height:1.05;color:var(--red);text-shadow:3px 3px 0 var(--red-dark)}
.ribbon{position:absolute;left:110px;top:262px;width:640px;height:84px}
.ribbon svg{position:absolute;left:0;top:0}
.ribbon-text{position:absolute;left:60px;top:8px;width:520px;text-align:center}
.ribbon-choir{font-style:italic;font-weight:700;font-size:21px;color:var(--white)}
.ribbon-director{font-weight:800;font-size:31px;color:var(--navy);line-height:1.2}
.sidebar{position:absolute;left:0;top:360px;width:205px;text-align:center}
.church-mark{display:flex;flex-direction:column;align-items:center;gap:8px;margin-top:10px}
.church-mark .dot{width:40px;height:40px;border-radius:50%;background:var(--ribbon-dark)}
.church-mark .name{font-weight:700;font-size:15px;line-height:1.2;color:var(--ribbon-dark);padding:0 14px}
.venue{margin-top:18px;font-weight:700;font-size:20px;line-height:1.25;color:var(--ink)}
.price{margin-top:16px;font-family:'Alfa Slab One',serif;font-size:32px;color:var(--red)}
.ticket-mark{margin:10px auto 0;width:150px;height:56px;background:var(--white);border-radius:8px;
  display:flex;align-items:center;justify-content:center;gap:8px}
.ticket-mark .square{width:16px;height:16px;background:var(--ribbon)}
.ticket-mark .name{font-weight:700;font-size:17px;color:var(--navy)}
.lede{position:absolute;left:232px;top:450px;width:600px;text-align:center;font-weight:700;font-size:20px;line-height:1.3;color:var(--ink)}
.portraits{position:absolute;left:245px;top:532px;display:flex;gap:6px}
.portrait{width:137px;height:148px;background:linear-gradient(160deg,#9a9a96,#3e3d3b)}
.playlist{position:absolute;left:0;top:700px;width:853px;height:448px;background:linear-gradient(var(--panel),var(--panel-dark))}
.cd-panel{position:absolute;left:0;top:0;width:205px;height:448px;background:rgba(0,0,0,.22);text-align:center;color:var(--white);padding-top:22px}
.cd-panel .label{font-weight:800;font-size:16px;text-transform:uppercase}
.cd-panel .blurb{font-weight:600;font-size:15px;line-height:1.3;margin-top:6px;padding:0 12px}
.cd-panel .blurb em{font-weight:700}
.cd-panel .offer{font-family:'Alfa Slab One',serif;font-size:44px;color:var(--red);margin-top:12px;line-height:1}
.cd-panel .rrp{font-size:14px;font-weight:600;margin-top:4px}
.cd-cover{width:150px;height:132px;margin:22px auto 0;background:linear-gradient(135deg,#6b5a44,#2a241d)}
.playlist-list{position:absolute;left:215px;top:36px;width:628px;text-align:center;font-family:'Roboto Slab',serif;font-weight:800;color:var(--cream)}
.playlist-list h2{font-size:30px;color:var(--white);text-transform:uppercase;margin-bottom:16px;font-weight:800}
.playlist-list li{list-style:none;font-size:28px;line-height:1.32;margin-bottom:10px}
.footer{position:absolute;left:0;top:1158px;width:853px;text-align:center;font-weight:600;font-size:14px;color:var(--ink)}
</style>
</head>
<body>
<div class="poster">
  <div class="date-bar"><span>22nd November 2013. 8pm</span></div>
  <h1 class="title">Ss Ottoline's Feast</h1>
  <div class="subtitle">Concert</div>

  <div class="ribbon">
    <svg width="640" height="84" viewBox="0 0 640 84" aria-hidden="true">
      <polygon points="0,20 50,20 50,84 0,84 18,52" fill="var(--ribbon-dark)"/>
      <polygon points="640,20 590,20 590,84 640,84 622,52" fill="var(--ribbon-dark)"/>
      <rect x="40" y="4" width="560" height="72" fill="var(--ribbon)"/>
    </svg>
    <div class="ribbon-text">
      <div class="ribbon-choir">Holy Ambrose by the Weir Stile</div>
      <div class="ribbon-director">Gil Pettifer-Rowe, Director</div>
    </div>
  </div>

  <aside class="sidebar">
    <div class="church-mark"><span class="dot"></span><span class="name">Holy Ambrose by the Weir Stile</span></div>
    <div class="venue">Norbury College Chapel, Oxford</div>
    <div class="price">Tickets: £5</div>
    <div class="ticket-mark"><span class="square"></span><span class="name">Seatpassly.net</span></div>
  </aside>

  <p class="lede">Celebrate the Patron Saint of Music and the prominent 20th century figures linked to her through life and death.</p>

  <div class="portraits">
    <div class="portrait" role="img" aria-label="Black and white portrait of Dorian Maltravers"></div>
    <div class="portrait" role="img" aria-label="Black and white portrait of R. T. Pembury"></div>
    <div class="portrait" role="img" aria-label="Black and white portrait of Walter G. Ashcombe"></div>
    <div class="portrait" role="img" aria-label="Black and white portrait of Perrine Vasholt"></div>
  </div>

  <section class="playlist">
    <div class="cd-panel">
      <div class="label">Also available:</div>
      <p class="blurb">The choir's latest 5-star reviewed CD <em>'The Harrowby Legacy'</em></p>
      <div class="offer">Just £8</div>
      <div class="rrp">(R.R.P. £12.95)</div>
      <div class="cd-cover" role="img" aria-label="Cover artwork of the CD The Harrowby Legacy"></div>
    </div>
    <div class="playlist-list">
      <h2>Playlist includes:</h2>
      <ul>
        <li>Dorian Maltravers's 'Carol for Ss Ottoline'</li>
        <li>K. D. Ruhnau's 'Geh, Seele, geh'</li>
        <li>Perrin Vasholt's 'The Lantern,'</li>
        <li>Cuthbert Fennimore's 'Lay down, dear one, in quiet rest'</li>
      </ul>
    </div>
  </section>

  <p class="footer">More information: www.gilpettiferrowe.com and www.habws.org.uk</p>
</div>
</body>
</html>
```